Essential oil label for bottles

Looking to modify our current logo and label design. It looks too simple. I will attach images of our competitors to use as examples. Our company name is Velnora. We have 2 different bottles. Clear and amber color. Going forward, we will be using only the amber bottle. The other 2 images are the biggest sellers brands. We want to make some adjustments to ours.

Target Market(s)

Brindex sales

Industry/Entity Type

Essential oil, perfume

Colors

Designer to choose only greyscale colors for use in the design.

Requirements
Nice to have
• A slight change to fonts and logo design. Maybe change the font and design of the word "Velnora" in our logo. Maybe add something to the label to make it stand out more but still keeping it clean and modern
Should not have
• No colors, besides, black, grays, whites, and off white.

```html
<!DOCTYPE html>
<html lang="en">
<head>
<meta charset="utf-8">
<title>Velnora – My Path Fragrance Oil Label</title>
<link rel="stylesheet" href="https://fonts.googleapis.com/css2?family=Josefin+Sans:wght@300&family=Bodoni+Moda:opsz,wght@6..96,700&display=swap">
<style>
  :root {
    --canvas-bg: #ffffff;
    --label-top: #2e2e2e;
    --label-mid: #1e1e1e;
    --label-bottom: #141414;
    --sheen: rgba(255, 255, 255, 0.07);
    --shade: rgba(0, 0, 0, 0.28);
    --ink-light: #f4f4f4;
    --ink-soft: #d6d6d6;
    --rule: #e6e6e6;
  }
  html, body {
    margin: 0;
    padding: 0;
    width: 1200px;
    height: 1200px;
    overflow: hidden;
    background: var(--canvas-bg);
  }
  .canvas {
    position: relative;
    width: 1200px;
    height: 1200px;
  }
  .label {
    position: absolute;
    left: 184px;
    top: 60px;
    width: 833px;
    height: 1080px;
    background:
      linear-gradient(90deg, var(--sheen) 0%, rgba(255,255,255,0.03) 35%, rgba(0,0,0,0) 60%, var(--shade) 100%),
      linear-gradient(180deg, var(--label-top) 0%, var(--label-mid) 50%, var(--label-bottom) 100%);
    color: var(--ink-light);
    font-family: "Josefin Sans", Arial, sans-serif;
    font-weight: 300;
    text-align: center;
    filter: grayscale(1);
    -webkit-font-smoothing: antialiased;
    will-change: transform;
  }
  .label__brand,
  .label__product,
  .label__type,
  .label__notes,
  .label__volume {
    position: absolute;
    left: 0;
    right: 0;
    margin: 0;
    line-height: 1;
    white-space: nowrap;
  }
  .label__brand {
    top: 134px;
    font-size: 64px;
    letter-spacing: 40px;
    padding-left: 40px;
  }
  .label__product {
    top: 445px;
    font-family: "Bodoni Moda", "Didot", serif;
    font-weight: 700;
    font-size: 117px;
    letter-spacing: 2px;
  }
  .label__rule {
    position: absolute;
    left: 138px;
    width: 556px;
    height: 2px;
    background: var(--rule);
  }
  .label__rule--top { top: 709px; }
  .label__rule--bottom { top: 883px; }
  .label__type {
    top: 750px;
    font-size: 66px;
    letter-spacing: 3px;
  }
  .label__notes {
    top: 824px;
    font-size: 25px;
    letter-spacing: 1px;
    color: var(--ink-soft);
  }
  .label__volume {
    top: 978px;
    font-size: 21px;
    letter-spacing: 1.5px;
    color: var(--ink-soft);
  }
</style>
</head>
<body>
  <main class="canvas">
    <section class="label">
      <p class="label__brand">VELNORA</p>
      <h1 class="label__product">MY PATH</h1>
      <div class="label__rule label__rule--top"></div>
      <p class="label__type">FRAGANCE OIL</p>
      <p class="label__notes">OUD WOOD | LEATHER | SANDALWOOD</p>
      <div class="label__rule label__rule--bottom"></div>
      <p class="label__volume">200 ML</p>
    </section>
  </main>
</body>
</html>
```